Pitch book for Birchvale Real Estate Investors.

Birchvale Investors is a new real estate investment company focused on multifamily (apartment) investments along the San Francisco Peninsula (in other parts of the world it is also referred to as flats). We need a professional Pitch Book i.e. brochure (digital and print) to raise equity from private investors. Read about “pitch book” on Wikipedia. The profile of the investor is conservative and must qualify as an accredited investor. Think high net worth individuals, CEOs and wealthy retiring couples. The investor that is attracted to real estate invest because it is low risk, produce cash flow and provide solid returns over the long term.

The brochure should convey trust, be highly professional and be clean and crisp. I attach a PowerPoint doc to be used as a copy for the brochure. I also attach a brochure of Harlow Pike – I like the look and feel, think it was designed with InDesign.

We will use the brochure at one-on-one meetings with investors where we will present on a laptop; we also need it in a format so that we can email it, print it and use it to be uploaded as a website.

I prefer the up and down scroll format (like you would do on a Mac) compared to PowerPoint but I am open to suggestions.

The photos I used in the PowerPoint presentation was found on the web, please use your own stock images.

Target Market(s)

High net worth individuals

Industry/Entity Type

Real Estate

Font styles to use
Serif

Requirements
Must have
• See attached Power Point
Nice to have
• See attached HPK brochure, I like the look and feel.
Should not have
• I am open to your ideas.

```html
<!DOCTYPE html>
<html lang="en">
<head>
<meta charset="utf-8">
<title>Birchvale Investors — Your Opportunity</title>
<link rel="stylesheet" href="https://fonts.googleapis.com/css2?family=Gowun+Batang&display=swap">
<style>
  :root {
    --page-bg: #2b2a2a;
    --text-light: #f4f4f2;
    --icon-white: #f7f7f7;
    --icon-shade: #c9c9c9;
    --pin-red: #e2323a;
    --photo-sky: #6f95c8;
    --photo-warm: #d9c59a;
    --photo-pink: #c7618f;
    --photo-street: #5a5450;
  }
  * { margin: 0; padding: 0; box-sizing: border-box; }
  html, body { width: 849px; height: 1200px; overflow: hidden; background: var(--page-bg); }
  .page {
    position: relative;
    width: 849px;
    height: 1200px;
    background: var(--page-bg);
    color: var(--text-light);
    font-family: "Gowun Batang", "Times New Roman", serif;
    overflow: hidden;
  }
  .section-icon { position: absolute; left: 28px; top: 70px; width: 82px; height: 82px; }
  .page-title {
    position: absolute;
    left: 85px;
    top: 68px;
    font-weight: 400;
    font-size: 37px;
    line-height: 38px;
    letter-spacing: 0.3px;
  }
  .page-title .subtitle { display: block; padding-left: 52px; }
  .intro {
    position: absolute;
    left: 59px;
    top: 192px;
    width: 700px;
    font-size: 25px;
    line-height: 29px;
    letter-spacing: 0.4px;
  }
  .pin-icon { position: absolute; left: 37px; top: 338px; width: 44px; height: 44px; }
  .section-heading {
    position: absolute;
    left: 100px;
    top: 344px;
    font-weight: 400;
    font-size: 33px;
    line-height: 40px;
  }
  .reasons {
    position: absolute;
    left: 59px;
    top: 405px;
    width: 732px;
    font-size: 25px;
    line-height: 31px;
    text-align: justify;
    letter-spacing: 0.3px;
  }
  .reasons p { margin-bottom: 36px; }
  .street-photo {
    position: absolute;
    left: 0;
    top: 705px;
    width: 849px;
    height: 423px;
    background:
      linear-gradient(180deg, var(--page-bg) 0%, var(--photo-sky) 10%, transparent 35%),
      linear-gradient(100deg, var(--photo-warm) 0%, var(--photo-warm) 45%, var(--photo-pink) 65%, #b98a6a 80%, var(--photo-street) 100%);
  }
  .brand {
    position: absolute;
    left: 14px;
    top: 1138px;
    display: flex;
    flex-direction: column;
    align-items: center;
    gap: 6px;
  }
  .brand-mark { width: 30px; height: 30px; background: var(--text-light); }
  .brand-name { font-size: 10px; line-height: 12px; color: var(--text-light); letter-spacing: 0.3px; }
</style>
</head>
<body>
<main class="page">
  <svg class="section-icon" viewBox="0 0 82 82" aria-hidden="true">
    <defs>
      <linearGradient id="iconFill" x1="0" y1="0" x2="1" y2="1">
        <stop offset="0" stop-color="var(--icon-white)"/>
        <stop offset="1" stop-color="var(--icon-shade)"/>
      </linearGradient>
    </defs>
    <path d="M12 0 H22 V48 A12 12 0 0 0 34 60 H82 V70 A12 12 0 0 1 70 82 H12 A12 12 0 0 1 0 70 V12 A12 12 0 0 1 12 0 Z" fill="url(#iconFill)"/>
  </svg>

  <h1 class="page-title">Your Opportunity<span class="subtitle">...safety, cash flow and appreciation</span></h1>

  <p class="intro">Birchvale Investors is pleased to offer you the opportunity to invest in the San Francisco Peninsula multifamily real estate market..</p>

  <svg class="pin-icon" viewBox="0 0 44 44" aria-hidden="true">
    <circle cx="22" cy="22" r="21" fill="#e8e8e8"/>
    <circle cx="22" cy="22" r="17" fill="#ffffff"/>
    <path d="M22 12 a7 7 0 0 1 7 7 c0 5 -7 13 -7 13 s-7 -8 -7 -13 a7 7 0 0 1 7 -7 Z" fill="var(--pin-red)"/>
    <circle cx="22" cy="19" r="2.6" fill="#ffffff"/>
  </svg>
  <h2 class="section-heading">Why invest and why here?</h2>

  <div class="reasons">
    <p>Investing in real estate is recognized as a significant wealth-creation strategy.</p>
    <p>The San Francisco Peninsula is one of the top real estate markets in the world.</p>
    <p>The multifamily asset class is considered a low risk investment.</p>
  </div>

  <div class="street-photo" role="img" aria-label="Photograph of a sunny San Francisco street lined with colourful Victorian apartment buildings"></div>

  <div class="brand">
    <span class="brand-mark"></span>
    <span class="brand-name">BIRCHVALE</span>
  </div>
</main>
</body>
</html>
```